Psychologist website

Simple psychologist website
Site map:
home
self-test
common conditions
children
contact
about
info

Current website:
http://www.corvalepsychology.com.au/

Not in love with logo, or colours etc - open brief
Happy for new font/style/logo for company name

Customer wants clean, credible and warm and friendly look & feel
stock photos OK

Brief:

One home page - simple with 2 or 3 small areas to tease and attract the user and one template page to suit all the other pages

Pages structurally similar to
http://www.wendlecourt.com.au/
In that the home page is different and the other pages are based on one template

Requirements
Must have
• 2 pages - one home page and one template page
• navigation for site map

```html
<!DOCTYPE html>
<html lang="en">
<head>
<meta charset="utf-8">
<title>Corvalepsychology</title>
<link href="https://fonts.googleapis.com/css2?family=Archivo+Black&family=Arimo:wght@400;700&family=Tinos&display=swap" rel="stylesheet">
<style>
  :root {
    --page: #ffffff;
    --brand-grey: #a9a9a9;
    --nav-top: #ffffff;
    --nav-bottom: #dcdada;
    --nav-edge: #b9b6b6;
    --nav-text: #555555;
    --body-text: #444444;
    --panel: #dddddd;
    --panel-line: #f4f4f4;
    --link-text: #5c5a12;
    --arrow: #cc2a10;
    --btn-top: #4fc43a;
    --btn-bottom: #1f8a15;
    --footer: #e0e0e0;
    --footer-text: #444444;
  }
  * { box-sizing: border-box; margin: 0; padding: 0; }
  html, body { width: 1200px; height: 1000px; overflow: hidden; background: var(--page); }
  .site { position: relative; width: 1200px; height: 1000px; }

  .brand {
    position: absolute; left: 108px; top: 274px;
    font-family: "Archivo Black", sans-serif; font-size: 38px;
    color: var(--brand-grey); letter-spacing: 0;
  }
  .hero-photo {
    position: absolute; top: 165px; height: 290px;
    background: linear-gradient(180deg, #f3f1f2 0%, #dfe3ec 55%, #c9cfdf 100%);
    border-radius: 70px 70px 0 0;
  }
  .hero-photo--doctor { left: 676px; width: 156px; }
  .hero-photo--clinician { left: 845px; width: 220px; background: linear-gradient(180deg, #f2f0f1 0%, #cfd5e6 55%, #a9b3cf 100%); }

  .main-nav {
    position: absolute; left: 102px; top: 457px; width: 979px; height: 41px;
    display: flex; list-style: none;
    background: linear-gradient(180deg, var(--nav-top) 0%, #f2f1f1 55%, var(--nav-bottom) 100%);
    border-left: 2px solid var(--nav-edge); border-right: 2px solid var(--nav-edge);
    border-bottom: 2px solid var(--nav-edge); border-radius: 0 0 5px 5px;
  }
  .main-nav li {
    height: 100%; padding: 9px 0 0 10px;
    font-family: "Arimo", sans-serif; font-weight: 700; font-size: 14px; color: var(--nav-text);
    border-right: 1px solid var(--nav-edge);
  }
  .main-nav li:last-child { border-right: 0; padding-left: 20px; }

  .feature-frame {
    position: absolute; left: 98px; top: 530px; width: 226px; height: 223px;
    background: linear-gradient(90deg, #cfcfcf, #f2f2f2 12%, #f2f2f2 88%, #cfcfcf);
  }
  .feature-photo {
    position: absolute; left: 19px; top: 5px; width: 188px; height: 213px;
    background: linear-gradient(180deg, #f4f3f6 0%, #e9e8ee 60%, #cfcdd6 100%);
  }
  .feature-text {
    position: absolute; left: 326px; top: 540px; width: 396px;
    font-family: "Tinos", serif; font-size: 14.6px; line-height: 19.2px; color: var(--body-text);
  }
  .learn-more {
    position: absolute; left: 614px; top: 730px; width: 108px; height: 27px;
    border-radius: 6px; background: linear-gradient(180deg, var(--btn-top), var(--btn-bottom));
    font-family: "Arimo", sans-serif; font-size: 12px; font-weight: 700; color: #fff;
    text-align: center; line-height: 27px; letter-spacing: 0.3px;
  }
  .divider { position: absolute; left: 96px; top: 787px; width: 631px; border-top: 1px dotted #999; }
  .intro-text {
    position: absolute; left: 96px; top: 797px; width: 634px;
    font-family: "Arimo", sans-serif; font-size: 15.4px; line-height: 18.2px; color: var(--body-text);
  }

  .quick-links {
    position: absolute; left: 761px; top: 518px; width: 321px; height: 346px;
    background: var(--panel); border-radius: 10px; padding-top: 40px; list-style: none;
  }
  .quick-links li {
    position: relative; height: 38px; border-top: 1px solid var(--panel-line);
    font-family: "Arimo", sans-serif; font-weight: 700; font-size: 13px; color: var(--link-text);
    padding: 2px 0 0 56px;
  }
  .quick-links li:last-child { border-bottom: 1px solid var(--panel-line); }
  .quick-links .arrow { position: absolute; left: 8px; top: 10px; }
  .quick-links .swoosh { position: absolute; right: 0; top: 0; }

  .site-footer {
    position: absolute; left: 85px; top: 955px; width: 1014px; height: 45px;
    background: var(--footer); padding: 12px 0 0 11px;
    font-family: "Tinos", serif; font-size: 17px; color: var(--footer-text); text-decoration: underline;
  }
</style>
</head>
<body>
<div class="site">
  <header>
    <div class="brand">Corvalepsychology</div>
    <div class="hero-photo hero-photo--doctor" role="img" aria-label="Stock photo of a doctor in a white coat with a stethoscope, arms folded"></div>
    <div class="hero-photo hero-photo--clinician" role="img" aria-label="Stock photo of a woman in a striped shirt holding a pen and a clipboard"></div>
    <ul class="main-nav">
      <li style="width:126px">Home</li>
      <li style="width:125px">Self-Test</li>
      <li style="width:125px">About</li>
      <li style="width:125px">Children</li>
      <li style="width:124px">Info</li>
      <li style="width:126px">Contact</li>
      <li style="width:224px">common conditions</li>
    </ul>
  </header>

  <main>
    <div class="feature-frame">
      <div class="feature-photo" role="img" aria-label="Stock photo of a man in shirt and tie raising one hand"></div>
    </div>
    <p class="feature-text">nolvera.com, based in India, offers all type design and web solutions.Our experience since 2010, we continue to provide our clients with the latest in website technology, development, and web design while offering functional, fast-loading, and visitor-friendly websites also provide logo design,wedding photography, wedding degital album making,fine arts and more.We can capture your vision and ideas and transform them into an effective design that is uniquely your own. We can produce design for you that is both modern and adaptable</p>
    <div class="learn-more">LEARN MORE</div>
    <div class="divider"></div>
    <p class="intro-text">nolvera.com, based in India, offers all type design and web solutions.Our experience since 2010, we continue to provide our clients with the latest in website technology, development, and web design while offering functional, fast-loading, and visitor-friendly websites also provide logo design,wedding photography, wedding degital album making,fine arts and more.We can capture your vision and ideas and transform them into an effective design that is uniquely your own. We can produce design for you that is both modern and adaptable</p>
  </main>

  <aside>
    <ul class="quick-links">
      <li><svg class="swoosh" width="140" height="20"><path d="M0 0 Q70 22 140 4 L140 0 Z" fill="#f4f4f4"/></svg><svg class="arrow" width="8" height="10"><path d="M0 0 L8 5 L0 10 Z" fill="#cc2a10"/></svg>Your Link1</li>
      <li><svg class="swoosh" width="140" height="20"><path d="M0 0 Q70 22 140 4 L140 0 Z" fill="#f4f4f4"/></svg><svg class="arrow" width="8" height="10"><path d="M0 0 L8 5 L0 10 Z" fill="#cc2a10"/></svg>Your Link2</li>
      <li><svg class="swoosh" width="140" height="20"><path d="M0 0 Q70 22 140 4 L140 0 Z" fill="#f4f4f4"/></svg><svg class="arrow" width="8" height="10"><path d="M0 0 L8 5 L0 10 Z" fill="#cc2a10"/></svg>Your Link3</li>
      <li><svg class="swoosh" width="140" height="20"><path d="M0 0 Q70 22 140 4 L140 0 Z" fill="#f4f4f4"/></svg><svg class="arrow" width="8" height="10"><path d="M0 0 L8 5 L0 10 Z" fill="#cc2a10"/></svg>Your Link4</li>
      <li><svg class="swoosh" width="140" height="20"><path d="M0 0 Q70 22 140 4 L140 0 Z" fill="#f4f4f4"/></svg><svg class="arrow" width="8" height="10"><path d="M0 0 L8 5 L0 10 Z" fill="#cc2a10"/></svg>Your Link5</li>
      <li><svg class="swoosh" width="140" height="20"><path d="M0 0 Q70 22 140 4 L140 0 Z" fill="#f4f4f4"/></svg><svg class="arrow" width="8" height="10"><path d="M0 0 L8 5 L0 10 Z" fill="#cc2a10"/></svg>Your Link6</li>
      <li><svg class="swoosh" width="140" height="20"><path d="M0 0 Q70 22 140 4 L140 0 Z" fill="#f4f4f4"/></svg><svg class="arrow" width="8" height="10"><path d="M0 0 L8 5 L0 10 Z" fill="#cc2a10"/></svg>Your Linl7</li>
    </ul>
  </aside>

  <footer class="site-footer">Copy right@www.quillbraeweb.us</footer>
</div>
</body>
</html>
```